Business Card Design

We do Metal Roofing, fascia and gutter and edge protection [safety rail].

Industry/Entity Type

Business

Contact Information for Business Card

Tallowind Roof Plumbing. Metal Roofing, Fascia and Gutter, Edge Protection
Corey 0458316072
Liam 0419563284
kv7lem4@tullanet.com
Lic: 618390K
ABN:57214603915

```html
<!DOCTYPE html>
<html lang="en">
<head>
<meta charset="utf-8">
<title>Tallowind Roof Plumbing — Business Card</title>
<link href="https://fonts.googleapis.com/css2?family=Fira+Sans:wght@500;600&display=swap" rel="stylesheet">
<style>
  :root {
    --backdrop: #e6e4e0;
    --card-white: #ffffff;
    --panel-dark: #23252f;
    --banner-yellow: #f7b43c;
    --banner-fold: #c98a1c;
    --icon-red: #c1272d;
    --ink: #26272e;
    --on-dark: #ffffff;
  }
  * { margin: 0; padding: 0; box-sizing: border-box; }
  html, body { width: 1200px; height: 900px; overflow: hidden; }
  body {
    background: var(--backdrop);
    font-family: "Fira Sans", sans-serif;
    color: var(--ink);
  }
  .card {
    position: absolute;
    left: 75px; top: 150px;
    width: 1050px; height: 600px;
    background: var(--card-white);
    overflow: hidden;
    box-shadow: 0 10px 30px rgba(0,0,0,0.18);
  }
  .card-shapes { position: absolute; inset: 0; }
  .panel { fill: var(--panel-dark); }
  .banner { fill: var(--banner-yellow); }
  .banner-fold { fill: var(--banner-fold); }
  .icon-disc { fill: var(--icon-red); }
  .icon-line { fill: none; stroke: #fff; stroke-width: 3; stroke-linejoin: round; stroke-linecap: round; }
  .icon-fill { fill: #fff; }

  .business-name {
    position: absolute;
    left: 440px; top: 105px;
    height: 80px;
    display: flex; align-items: center;
    font-size: 40px; font-weight: 500;
    letter-spacing: 1px;
    text-transform: uppercase;
    white-space: nowrap;
  }
  .brand-mark {
    position: absolute;
    left: 60px; top: 262px;
    width: 290px;
    display: flex; align-items: center; justify-content: center; gap: 12px;
    color: var(--on-dark);
    font-size: 32px; font-weight: 600;
    letter-spacing: 2px;
  }
  .brand-square {
    width: 18px; height: 18px;
    background: var(--banner-yellow);
  }
  .services {
    position: absolute;
    left: 60px; top: 350px;
    width: 290px;
    text-align: center;
    color: var(--on-dark);
    font-size: 21px; font-weight: 500;
    line-height: 1.2;
    text-transform: uppercase;
    letter-spacing: 0.5px;
  }
  .contact-line {
    position: absolute;
    left: 610px;
    font-size: 25px; font-weight: 500;
    letter-spacing: 1px;
    text-transform: uppercase;
    line-height: 1.25;
  }
  .phones { top: 290px; }
  .email { top: 403px; }
  .registration {
    position: absolute;
    right: 100px; top: 492px;
    font-size: 19px; font-weight: 600;
    letter-spacing: 0.5px;
    text-transform: uppercase;
  }
</style>
</head>
<body>
  <main class="card">
    <svg class="card-shapes" width="1050" height="600" viewBox="0 0 1050 600" aria-hidden="true">
      <polygon class="panel" points="0,0 470,0 330,600 0,600"/>
      <rect class="banner" x="380" y="105" width="670" height="80"/>
      <polygon class="banner-fold" points="380,185 425,185 425,220"/>
      <!-- phone icon -->
      <circle class="icon-disc" cx="560" cy="322" r="28"/>
      <path class="icon-fill" d="M549 309c2-2 4-2 5 0l3 5c1 2 0 3-1 4l-2 2c1 3 4 6 7 7l2-2c1-1 2-2 4-1l5 3c2 1 2 3 0 5l-3 3c-3 2-9 0-15-6s-8-12-6-15z"/>
      <!-- mail icon -->
      <circle class="icon-disc" cx="560" cy="420" r="28"/>
      <rect class="icon-line" x="545" y="409" width="30" height="22" rx="2"/>
      <path class="icon-line" d="M545 411l15 11 15-11M545 430l11-9M575 430l-11-9"/>
    </svg>

    <h1 class="business-name">Tallowind Roof Plumbing</h1>

    <div class="brand-mark"><span class="brand-square"></span>TALLOWIND</div>
    <p class="services">Metal Roofing,<br>Fascia and Gutter,<br>Edge Protection</p>

    <p class="contact-line phones">Corey 0458316072<br>Liam 0419563284</p>
    <p class="contact-line email">kv7lem4@tullanet.com</p>
    <p class="registration">Lic: 618390K ABN:57214603915</p>
  </main>
</body>
</html>
```